Lumawerks Business Card Design

I need a business card design for a new Business, that is focused on Custom Made Designer Furniture. that is aimed at the mid to high end markets. I would like a card that would in some way portray what I do for my clients in the way we are able to make any idea a reality and also work within a set budget to meet their requirements.
I like quite contemporary colours and styling and I want the final design to communicate a Contemporary and Professional image.

Target Market(s)

mid to high end market

Industry/Entity Type

Business

Contact Information for Business Card

Lumawerks
Darren Holtzmann
18 Wexbury Rd, Kelston, Auckland, New Zealand 0712.

Requirements
Nice to have
• I would also like to utilize the spot gloss or raised print on my cards

```html
<!DOCTYPE html>
<html lang="en">
<head>
<meta charset="utf-8">
<title>Lumawerks Business Card</title>
<link rel="stylesheet" href="https://fonts.googleapis.com/css2?family=Lexend:wght@300;400;500&display=swap">
<style>
  :root {
    --backdrop: #c9cacd;
    --card: #ffffff;
    --ink: #000000;
    --teal: #1ba49b;
    --band: #000000;
  }
  * { margin: 0; padding: 0; box-sizing: border-box; }
  html, body {
    width: 1200px;
    height: 1000px;
    overflow: hidden;
    background: var(--backdrop);
    font-family: "Lexend", sans-serif;
  }
  .business-card {
    position: absolute;
    left: 177px;
    top: 244px;
    width: 847px;
    height: 513px;
    background: var(--card);
    overflow: hidden;
  }
  .holder-name {
    position: absolute;
    left: 52px;
    top: 124px;
    font-size: 27px;
    font-weight: 500;
    color: var(--ink);
    letter-spacing: 0.2px;
  }
  .contact-list {
    position: absolute;
    left: 52px;
    top: 202px;
    list-style: none;
    font-size: 27px;
    font-weight: 300;
    color: var(--ink);
    line-height: 40px;
  }
  .contact-item {
    display: grid;
    grid-template-columns: 52px auto;
    margin-bottom: 2px;
  }
  .contact-label {
    color: var(--teal);
    font-weight: 500;
  }
  .brand {
    position: absolute;
    right: 59px;
    top: 180px;
    display: flex;
    align-items: center;
    gap: 12px;
  }
  .brand-square {
    width: 34px;
    height: 34px;
    background: var(--ink);
  }
  .brand-name {
    font-size: 34px;
    font-weight: 500;
    color: var(--ink);
  }
  .tagline-band {
    position: absolute;
    left: 0;
    bottom: 0;
    width: 847px;
    height: 74px;
  }
  .tagline {
    position: absolute;
    left: 0;
    bottom: 18px;
    width: 847px;
    text-align: center;
    font-size: 28px;
    font-weight: 300;
    color: var(--teal);
    letter-spacing: 0.3px;
  }
</style>
</head>
<body>
  <section class="business-card">
    <h1 class="holder-name">Darren Holtzmann</h1>

    <ul class="contact-list">
      <li class="contact-item"><span class="contact-label">A:</span><span>18 Wexbury Rd, Kelston,<br>Auckland, New Zealand 0712</span></li>
      <li class="contact-item"><span class="contact-label">P:</span><span>(09) 999 9999</span></li>
      <li class="contact-item"><span class="contact-label">M:</span><span>021 000 0000</span></li>
      <li class="contact-item"><span class="contact-label">E:</span><span>name@domain.co.nz</span></li>
    </ul>

    <div class="brand">
      <span class="brand-square"></span>
      <span class="brand-name">Lumawerks</span>
    </div>

    <svg class="tagline-band" viewBox="0 0 847 74" aria-hidden="true">
      <path d="M0 74 C0 30 30 0 80 0 L847 0 L847 74 Z" fill="var(--band)"/>
    </svg>
    <p class="tagline">custom designed furniture to fit any budget</p>
  </section>
</body>
</html>
```